Whitcombe Ellery Foundation Flyer

Design a two sided flyer that will be used to solicit charitable donations from local residents and businesses for a new school gymnasium. The fundraising project is being done by the Whitcombe Ellery Foundation. I have attached two files for: 1. "Original" Flyer 2. "Revised" Copy. Please use "revised" for the copy. You can refer to "original" for illustrations and pictures. The Whitcombe Ellery Foundation does not have a logo, so you can create one. It should be simple and understated.

```html
<!DOCTYPE html>
<html lang="en">
<head>
<meta charset="utf-8">
<title>Whitcombe Ellery Foundation Flyer</title>
<link href="https://fonts.googleapis.com/css2?family=Bebas+Neue&family=Oswald:wght@500;600&family=Poppins:wght@400;500;600&family=Allura&display=swap" rel="stylesheet">
<style>
:root{
  --gold:#d5a758;
  --bronze:#9b7431;
  --ink:#111111;
  --paper:#ffffff;
  --backdrop:#c9c9c9;
  --muted:#cfcfcf;
  --body:#222222;
}
*{margin:0;padding:0;box-sizing:border-box}
html,body{width:1200px;height:888px;overflow:hidden;background:var(--backdrop)}
body{position:relative;font-family:"Poppins",sans-serif;color:var(--body)}
.page{position:absolute;top:123px;width:494px;height:640px;background:var(--paper);overflow:hidden}
.page--front{left:86px}
.page--back{left:627px}
.abs{position:absolute}
.header-band{left:0;top:0;width:494px;height:112px;background:var(--gold)}
.brand{left:20px;top:26px;width:140px;text-align:center}
.brand__mark{display:block;width:36px;height:36px;margin:0 auto 6px;background:var(--ink)}
.brand__name{font-family:"Bebas Neue",sans-serif;font-size:17px;letter-spacing:.5px;color:var(--ink);line-height:1}
.brand__sub{font-size:5.5px;letter-spacing:2.5px;color:var(--ink);margin-top:2px}
.divider{left:163px;top:24px;width:1px;height:68px;background:var(--paper)}
.kicker{left:177px;top:24px;font-size:11px;letter-spacing:1px;color:var(--ink);font-weight:500}
.headline{left:177px;top:38px;font-family:"Bebas Neue",sans-serif;font-size:42px;line-height:1;color:var(--paper)}
.name-plate{left:268px;top:84px;width:226px;height:46px;background:var(--ink);font-family:"Bebas Neue",sans-serif;font-size:34px;color:var(--gold);text-align:center;line-height:48px;letter-spacing:1px}
.photo{background:linear-gradient(100deg,#ffffff 0%,#d6d6d6 30%,#8d8d8d 70%,#5a5a5a 100%)}
.photo--dark{background:linear-gradient(90deg,#f4f4f4 0%,#bdbdbd 45%,#6e6e6e 100%)}
.col{left:34px;width:210px}
h3{font-family:"Oswald",sans-serif;font-weight:500;font-size:9.5px;color:var(--ink);text-transform:uppercase;margin-bottom:3px}
p{font-size:5.6px;line-height:1.38;margin-bottom:5px}
.lead{color:var(--bronze);font-weight:600;font-size:6.4px;line-height:1.3}
.quote{border-left:1.5px solid var(--gold);padding-left:7px}
.vision{left:0;top:411px;width:240px;height:77px;background:var(--bronze);padding:9px 20px 0 34px;color:var(--paper)}
.vision h3{color:var(--ink)}
.vision p{color:var(--paper)}
.dark-base{left:0;top:472px;width:494px;height:168px;background:linear-gradient(180deg,#2a2a2a 0%,#111 40%,#0c0c0c 100%)}
.dark-col{width:205px;color:var(--muted)}
.dark-col h3{color:var(--gold)}
.dark-col p{color:#bdbdbd}
.footer-rule{left:35px;top:582px;width:424px;height:1px;background:#555}
.footer-note{left:35px;top:591px;font-size:5.5px;letter-spacing:.8px;color:#cfcfcf}
.footer-name{left:35px;top:600px;font-family:"Oswald",sans-serif;font-size:13px;color:var(--gold)}
.footer-name span{font-family:"Poppins",sans-serif;font-size:5.5px;letter-spacing:1.5px;color:#ddd;margin-left:6px;vertical-align:middle}
.footer-org{right:35px;top:591px;font-size:5.6px;letter-spacing:2px;color:var(--gold);text-align:right}
.footer-contact{right:35px;top:604px;font-size:10px;font-weight:600;color:var(--paper);text-align:right}
.footer-contact small{font-size:6px;font-weight:500;margin-left:6px}
.footer-contact svg{vertical-align:middle;margin-left:4px}
.sponsor-title{left:203px;top:24px;font-family:"Bebas Neue",sans-serif;font-size:25px;color:var(--paper);line-height:1}
.sponsor-copy{left:203px;top:51px;width:270px;font-size:5.6px;line-height:1.3;color:var(--ink)}
.sponsor-copy b{font-size:7px}
.donate-col{left:32px;top:112px;width:151px;height:355px;background:var(--bronze)}
.donate-title{left:53px;top:130px;font-family:"Bebas Neue",sans-serif;font-size:38px;line-height:.95;color:var(--paper)}
.tab{left:27px;width:100px;height:22px;background:var(--ink);font-family:"Oswald",sans-serif;font-size:10px;color:var(--paper);padding:4px 0 0 26px}
.tab-text{left:53px;width:120px;font-size:8.8px;line-height:1.2;color:var(--paper)}
.right-col{left:203px;width:275px}
.right-col h3{font-size:10px}
.right-col p{font-size:7px;color:var(--ink)}
.gold-caps{font-size:6.6px;letter-spacing:1.2px;font-weight:600;color:var(--gold);margin-bottom:2px}
.handle{font-size:7px;letter-spacing:1px;color:var(--ink)}
.social-box{left:203px;top:347px;width:252px;height:22px;border:1px solid var(--gold);padding:2px 0 0 8px;font-family:"Oswald",sans-serif;font-size:11px;letter-spacing:1.5px;color:var(--ink);display:flex;align-items:center;gap:8px}
.social-box i{display:inline-block;width:9px;height:9px;border-radius:50%;background:var(--bronze)}
.together{left:0;top:476px;width:494px;text-align:center;color:var(--paper);font-size:8.8px;font-weight:600}
.together em{font-family:"Allura",cursive;font-style:normal;font-size:20px;color:var(--gold);font-weight:400;margin-right:4px}
.together-copy{left:38px;top:512px;width:418px;text-align:center;font-size:5.6px;line-height:1.35;color:#ccc}
.thanks{left:0;top:537px;width:494px;text-align:center;font-family:"Allura",cursive;font-size:15px;color:var(--paper)}
.signoff{left:0;top:562px;width:494px;text-align:center;font-size:8px;letter-spacing:1.5px;color:#ddd}
.signoff b{color:var(--gold);letter-spacing:0;margin-left:4px}
</style>
</head>
<body>

<section class="page page--front">
  <div class="abs header-band"></div>
  <div class="abs brand"><span class="brand__mark"></span><div class="brand__name">WHITCOMBE ELLERY</div><div class="brand__sub">FOUNDATION</div></div>
  <div class="abs divider"></div>
  <div class="abs kicker">LIFTING OUR COMMUNITY &amp; HONORING</div>
  <div class="abs headline">THE LIFE &amp; LEGACY OF</div>
  <div class="abs photo" style="left:200px;top:112px;width:294px;height:360px" role="img" aria-label="Black and white photo of a gymnast doing a handstand in a gym"></div>
  <div class="abs name-plate">WHITCOMBE ELLERY</div>

  <div class="abs col" style="top:128px">
    <h3>Why build a gymnasium?</h3>
    <p class="lead">One small community can come together in support of our Island youth.</p>
    <p>In July 2023, our community tragically lost Whitcombe Ellery in a horrific motorcycle accident. In tribute to Whitcombe's remarkable spirit and love for the Larkspur Island school, the Whitcombe Ellery Foundation (a 501(c)(3) foundation) is seeking to lift our community and provide a much-needed facility for our community and students by building a much needed school gymnasium in Whitcombe's honor.</p>
    <p>Currently, the school district doesn't have an onsite gym. Students hold gym classes, practices, and scrimmages at a rented community gym which is a short walk from the school. The new gymnasium would benefit the students and community as well as serve as a living memorial to Whitcombe and other students who left us far too soon.</p>
    <p>The new gym will be a place for our Island youth to have physical education classes as well as a place for our student-athletes to compete and host visiting teams.</p>
  </div>

  <div class="abs col" style="top:327px;width:212px">
    <h3>Dear community members, friends &amp; supporters</h3>
    <p class="quote">We invite you to join us in this journey of love and community that celebrates the life and legacy of a beloved local resident, Whitcombe Ellery. Whitcombe's unwavering love for Larkspur Island and his profound belief in the power of community has inspired us to embark on this heartfelt initiative to build a new school gymnasium in his honor.</p>
  </div>

  <div class="abs dark-base"></div>
  <div class="abs vision">
    <h3>The Vision</h3>
    <p>The Whitcombe Ellery Memorial Gymnasium Concept will be an onsite facility that will be approximately 12,000 square feet and will cost <b>$4.5 million</b>. Attached directly to the school it will include a gymnasium with proper room for spectators, entry lobby, concession area, two team locker rooms and an equipment storage room</p>
  </div>

  <div class="abs dark-col" style="left:35px;top:502px">
    <h3>How you can help</h3>
    <p>To bring this vision to life, we need your help! We're reaching out to ask for your generous donations to help fund the gym's construction. Your contribution will not only honor Whitcombe's memory but will also create a lasting legacy that benefits our Island, our Students and our community.</p>
  </div>
  <div class="abs dark-col" style="left:261px;top:502px;width:210px">
    <h3>Why can't the school pay?</h3>
    <p>The combination of revenue limits and sparse state aid has left many Northland schools unable to meet their operational needs. Larkspur Island is one of the state's most severely underfunded school districts! This is NOT because they overspend but because they are severely underfunded. The school has no choice but to run on a bare-bones budget.</p>
  </div>

  <div class="abs footer-rule"></div>
  <div class="abs footer-note">For more information,please reach out to:</div>
  <div class="abs footer-name">HARRIET ELLERY<span>PRESIDENT</span></div>
  <div class="abs footer-org">WHITCOMBE ELLERY MEMORIAL FOUNDATION</div>
  <div class="abs footer-contact">555-014-0081<svg width="7" height="5" viewBox="0 0 7 5"><rect width="7" height="5" fill="#d5a758"/><path d="M0 0l3.5 3L7 0" stroke="#111" stroke-width=".8" fill="none"/></svg><small>info@whitcombeellery.org</small></div>
</section>

<section class="page page--back">
  <div class="abs header-band"></div>
  <div class="abs brand"><span class="brand__mark"></span><div class="brand__name">WHITCOMBE ELLERY</div><div class="brand__sub">FOUNDATION</div></div>
  <div class="abs sponsor-title">SPONSORSHIP OPPORTUNITIES</div>
  <div class="abs sponsor-copy">We also offer sponsorship opportunities for individuals and businesses looking to make a significant impact. Sponsorships for various areas within the gymnasium and special recognition in our community events are available. For more information on sponsorships, please contact us at<br><b>(555) 014-2290 or email hello@whitcombeelleryfoundation.org.</b></div>

  <div class="abs photo--dark" style="left:183px;top:282px;width:311px;height:190px" role="img" aria-label="Black and white photo of a gymnast stretching on a mat"></div>
  <div class="abs dark-base" style="top:460px;height:180px"></div>

  <div class="abs donate-col"></div>
  <div class="abs donate-title">WAYS TO<br>DONATE</div>
  <div class="abs tab" style="top:207px">ONLINE</div>
  <div class="abs tab-text" style="top:236px">Payment app (address to come)</div>
  <div class="abs tab" style="top:266px">IN-PERSON</div>
  <div class="abs tab-text" style="top:293px">Donations can be made at the front office of the Larkspur Island School, located at 42 Harbor Street.</div>
  <div class="abs tab" style="top:371px">MAIL</div>
  <div class="abs tab-text" style="top:396px">Send checks payable to "Whitcombe Ellery Foundation" to P.O. Box 318, Larkspur Island, NL 00418</div>

  <div class="abs right-col" style="top:138px">
    <h3>Upcoming fundraising events</h3>
    <p>Join us for a series of events to raise funds and celebrate Whitcombe's life:</p>
    <div class="gold-caps" style="margin-top:8px">FOLLOW OUR SOCIAL PAGE FOR UPDATES &amp; EVENTS</div>
    <div class="handle">@WHITCOMBE ELLERY FOUNDATION</div>
  </div>
  <div class="abs right-col" style="top:225px">
    <h3>Stay connected</h3>
    <p>Follow our progress and stay updated on upcoming events by visiting our website and following us on social media.</p>
  </div>
  <div class="abs social-box"><i></i>@WHITCOMBE ELLERY FOUNDATION</div>

  <div class="abs together"><em>Together</em>LET'S BUILD SOMETHING SPECIAL</div>
  <div class="abs together-copy">Whitcombe Ellery's legacy is one of vitality, inspiration, and Island Community Spirit. Let's honor him by creating a place where his values continue to thrive and where everyone can feel good about our Island Community and meet the needs of our children and students. Your support is crucial to making this dream a reality.</div>
  <div class="abs thanks">Thank you for your generosity and commitment to our community</div>
  <div class="abs signoff">WITH HEARTFELT GRATITUDE<b>The Whitcombe Ellery Foundation</b></div>

  <div class="abs footer-rule"></div>
  <div class="abs footer-note">For more information,please reach out to:</div>
  <div class="abs footer-name">HARRIET ELLERY<span>PRESIDENT</span></div>
  <div class="abs footer-org">WHITCOMBE ELLERY MEMORIAL FOUNDATION</div>
  <div class="abs footer-contact">555-014-0081<svg width="7" height="5" viewBox="0 0 7 5"><rect width="7" height="5" fill="#d5a758"/><path d="M0 0l3.5 3L7 0" stroke="#111" stroke-width=".8" fill="none"/></svg><small>info@whitcombeellery.org</small></div>
</section>

</body>
</html>
```